Regional Sales Company Needs Professional Document Design

We are an American Midwest company that needs clean, polished document layouts that effectively communicate the most critical information to the recipient. This project is specifically for a sales quote, but additional documents (subsequent work) need a consistent look. Our primary design guidelines are: 1) Use the same colors and logos provided. 2) minimize the amount of space the header occupies on the document. 3) Prioritize the information as it has been numbered in the attachment (1 - 5). 4) Redesign the footer logo/image. The information must stay the same, but present it as you see fit.

I have attached a draft and an annotation layout. The draft shows the overall structure and information on the document. The Annotation layout has the numbering referenced and some additional notes.

Industry/Entity Type

HVAC Supplier

Colors
0054AA
0677BA
7BADD7
CADEEF
E8F1F8

Requirements
Must have
• Maintain overall structure of draft. E.g. No left to right documents

```html
<!DOCTYPE html>
<html lang="en">
<head>
<meta charset="utf-8">
<title>Sales Quote – Keystone Supply</title>
<link href="https://fonts.googleapis.com/css2?family=Montserrat:wght@400;500;600;700;800&family=Open+Sans:wght@400;600;700&display=swap" rel="stylesheet">
<style>
  :root{
    --navy:#0054AA;
    --blue:#0677BA;
    --sky:#7BADD7;
    --mist:#CADEEF;
    --ice:#E8F1F8;
    --ink:#2b3340;
    --muted:#6b7480;
    --panel:#eef1f4;
    --page:#ffffff;
  }
  *{box-sizing:border-box;margin:0;padding:0}
  html,body{width:763px;height:1200px;overflow:hidden;background:var(--page)}
  body{font-family:"Open Sans",Arial,sans-serif;color:var(--ink);position:relative}
  .quote{position:absolute;inset:0;padding:44px 48px 0}

  .header{display:flex;justify-content:space-between;align-items:flex-start;height:96px}
  .brand{display:flex;align-items:center;gap:10px;margin-top:22px}
  .brand-square{width:18px;height:18px;background:var(--navy)}
  .brand-name{font-family:"Montserrat",sans-serif;font-weight:700;font-size:24px;color:var(--navy);line-height:1;letter-spacing:-.3px}
  .project{width:336px;background:var(--panel);padding:10px 16px;text-align:right;font-size:10px;line-height:1.45;color:var(--ink)}
  .project h1{font-family:"Montserrat",sans-serif;font-size:15px;font-weight:700;color:var(--ink);margin-bottom:2px}
  .project b{color:var(--navy)}

  .tagline{margin-top:-4px;width:330px;background:var(--navy);color:#fff;font-family:"Montserrat",sans-serif;font-size:8px;font-weight:600;letter-spacing:3px;padding:4px 14px;text-transform:uppercase}

  .dates{display:flex;gap:36px;margin-top:22px;font-size:10.5px;border-bottom:1px solid var(--mist);padding-bottom:12px}
  .dates span b{color:var(--ink)}
  .dates .v{color:var(--blue);margin-left:4px}
  .dates .push{margin-left:auto}

  .cols{display:flex;margin-top:36px;font-family:"Montserrat",sans-serif;font-size:14px;font-weight:600;color:var(--blue)}
  .cols .mfr{width:215px;padding-left:26px}
  .cols .desc{flex:1;text-align:center}

  .line-item{display:flex;align-items:center;margin-top:18px}
  .line-item .maker{width:215px;display:flex;align-items:center;gap:8px;padding-left:26px}
  .maker-sq{width:16px;height:16px;background:var(--navy)}
  .maker-name{font-family:"Montserrat",sans-serif;font-weight:800;font-size:20px;color:var(--ink);letter-spacing:-.3px}
  .item-box{flex:1;background:var(--panel);padding:12px 18px;font-size:8.5px;line-height:1.55;color:var(--ink)}
  .item-box .qty{font-weight:700;color:var(--navy)}
  .item-box .total{margin-top:8px;font-weight:700;color:var(--ink)}
  .item-box .price{font-weight:700;color:var(--blue)}
  .item-box p{margin-top:6px}

  .footer{position:absolute;left:48px;right:48px;bottom:52px}
  .footer-band{background:var(--navy);color:#fff;text-align:center;font-family:"Montserrat",sans-serif;font-weight:600;font-size:11px;padding:7px 0}
  .offices{display:flex;background:var(--blue);color:#fff;padding:12px 10px;font-size:8px;line-height:1.5;text-align:center}
  .office{flex:1}
  .office h3{font-family:"Montserrat",sans-serif;font-size:9px;font-weight:700;margin-bottom:2px}
  .office + .office{border-left:1px solid var(--sky)}
</style>
</head>
<body>
<main class="quote">
  <header class="header">
    <div class="brand">
      <span class="brand-square"></span>
      <span class="brand-name">Keystone Supply</span>
    </div>
    <section class="project">
      <h1>Maple Ridge Care Center</h1>
      <div>1450 Orchard Lane, Cedar Falls, OH 44210</div>
      <div><b>Quote:</b> Q-24-0318</div>
      <div><b>Engineer:</b> Bright Line Engineering</div>
    </section>
  </header>
  <div class="tagline">Air · Comfort · Solutions · Service</div>

  <section class="dates">
    <span><b>Quote Date:</b><span class="v">03/18/2024</span></span>
    <span><b>Project Bid Date:</b><span class="v">03/29/2024</span></span>
    <span class="push"><b>Addendum:</b><span class="v">1</span></span>
    <span><b>Plan Date:</b><span class="v">02/26/2024</span></span>
  </section>

  <div class="cols"><div class="mfr">Manufacturer</div><div class="desc">Qty Description</div></div>

  <article class="line-item">
    <div class="maker"><span class="maker-sq"></span><span class="maker-name">Vantage</span></div>
    <div class="item-box">
      <div><span class="qty">44</span> · Square ceiling diffusers with white finish and opposed blade dampers</div>
      <div>Includes border type 3 for lay-in ceiling grid, sized per schedule</div>
      <div>Return grilles with fixed louvers and aluminum frame</div>
      <div>Excludes installation, wiring and field painting</div>
      <div class="total">TOTAL NET F.O.B. FACTORY: <span class="price">$6,840</span></div>
    </div>
  </article>

  <article class="line-item">
    <div class="maker"><span class="maker-sq"></span><span class="maker-name">Northvent</span></div>
    <div class="item-box">
      <div><span class="qty">1</span> · Rooftop energy recovery unit with supply and exhaust fans, enthalpy wheel, filters, electric preheat, direct drive motors, factory disconnect, and controls package per schedule</div>
      <p>Unit shipped in one section with curb adapter and vibration isolation rails</p>
      <p>Includes start-up assistance and one year parts warranty</p>
      <p>Includes BACnet interface and space sensors for remote monitoring</p>
      <p>Excludes field wiring, crane, rigging and roof curb installation</p>
      <div class="total">TOTAL NET F.O.B. FACTORY: <span class="price">$48,260</span></div>
      <p><span class="qty">2</span> · Inline cabinet exhaust fans with speed control and backdraft dampers</p>
      <div class="total">TOTAL NET F.O.B. FACTORY: <span class="price">$3,415</span></div>
    </div>
  </article>

  <article class="line-item">
    <div class="maker"><span class="maker-sq"></span><span class="maker-name">Northvent</span></div>
    <div class="item-box">
      <div><span class="qty">3</span> · Wall mounted propeller fans with guards and motorized shutters</div>
      <div class="total">TOTAL NET F.O.B. FACTORY: <span class="price">$2,190</span></div>
    </div>
  </article>

  <footer class="footer">
    <div class="footer-band">Partnering With You Delivering Solutions and Service</div>
    <div class="offices">
      <div class="office"><h3>Columbus</h3>410 River Park Dr, Columbus, OH<br>(555) 014-2210</div>
      <div class="office"><h3>Dayton</h3>88 Commerce Way, Dayton, OH<br>(555) 014-3320</div>
      <div class="office"><h3>Toledo</h3>1201 Harbor Ave, Toledo, OH<br>(555) 014-4430</div>
    </div>
  </footer>
</main>
</body>
</html>
```